VORELLO - PIZZA - RESTAURANT PIZZERIA

Flyer format:
- A5 front / back leaflet (Example attachment)
Customer logos:
- Attachment, VORELLO PIZZA logo
Address and contact to put on the flyers:
- Phone to add: (+352) 26 58 40 71 (Page 1)
- Address to be added: 27 rue des tilleuls, L-3829 Kayl, Luxembourg (Page 1)
- Website: www.vorello-example.lu (Page 1)
- Leave a space for the timetable (last page)
Flyer color:
- Preferably black background with colored customer logo
Typefaces:
- At your convenience
Descriptions:
- We would like to have a flyer to the one we have put as an example in the attachment
Important elements:
- Pizza oven on the cover page with customer logo, address and contact details
- The graphic elements must be usable and non-paying, we want a quality visual.
- Menu (attachment) The menu is in Word format, it must be laid out in a thoughtful way as on the example model.
- We need to find some pizza and/or ingredient visuals
Aspects :
- The design of the set must be elegant, sober and must contain all the information (Menu, visual of your choice, logo)

Target Market(s)

Private and professional public

Font styles to use
Serif
Sans Serif

Requirements
Must have
• Elegance, take into account the information of the comment
Nice to have
• Pizza oven, Dominant color black, Gold, red
Should not have
• poor quality visuals

```html
<!DOCTYPE html>
<html lang="fr">
<head>
<meta charset="utf-8">
<title>Vorello Pizza – Menu</title>
<link href="https://fonts.googleapis.com/css2?family=Fira+Sans:ital,wght@0,600;1,400;1,500;1,600&family=Righteous&family=Cormorant+Garamond:ital,wght@0,500;1,500&display=swap" rel="stylesheet">
<style>
  :root {
    --bg-dark: #050505;
    --bg-warm: #2b2218;
    --gold: #e5b33a;
    --gold-soft: #d9a83c;
    --yellow: #f2c21a;
    --red: #c0262d;
    --white: #ffffff;
    --cream: #f3ede2;
  }
  * { margin: 0; padding: 0; box-sizing: border-box; }
  html, body { width: 1200px; height: 846px; overflow: hidden; background: var(--bg-dark); }
  .flyer {
    position: relative; width: 1200px; height: 846px; overflow: hidden;
    background: radial-gradient(ellipse at 78% 45%, var(--bg-warm) 0%, #1a140f 40%, var(--bg-dark) 75%);
    font-family: "Fira Sans", Arial, sans-serif; font-style: italic; color: var(--white);
  }
  .banner { position: absolute; }
  .banner svg { position: absolute; inset: 0; }
  .banner span {
    position: absolute; top: 50%; left: 0; right: 0; transform: translateY(-50%);
    text-align: center; font-family: "Righteous", sans-serif; font-style: normal;
    color: var(--gold); font-size: 31px; letter-spacing: 1.5px;
  }
  .banner-desserts { left: 22px; top: 24px; width: 262px; height: 48px; }
  .banner-boissons { left: 334px; top: 22px; width: 272px; height: 48px; }
  .banner-supplements { left: 22px; top: 266px; width: 334px; height: 48px; }

  .menu { position: absolute; list-style: none; }
  .menu li { display: flex; align-items: baseline; height: 21.9px; font-size: 18px; }
  .menu .name { color: var(--gold); font-weight: 500; white-space: nowrap; }
  .menu .name em { color: var(--white); font-weight: 400; margin-left: 12px; }
  .menu .leader { flex: 1; border-bottom: 2px dotted var(--white); margin: 0 5px 5px; min-width: 10px; }
  .menu .price { color: var(--white); font-weight: 600; white-space: nowrap; }

  .desserts { left: 48px; top: 80px; width: 278px; }
  .desserts li { height: 22px; }

  .drinks { position: absolute; left: 358px; top: 82px; width: 222px; }
  .drink-group { margin-bottom: 10px; }
  .drink-head { display: flex; align-items: baseline; font-size: 18px; height: 22px; }
  .drink-head .name { color: var(--gold); font-weight: 500; white-space: nowrap; }
  .drink-head .leader { flex: 1; border-bottom: 2px dotted var(--white); margin: 0 5px 5px; }
  .drink-head .price { font-weight: 600; white-space: nowrap; }
  .drink-list { font-size: 17.5px; line-height: 21.9px; }

  .sub-title {
    position: absolute; font-size: 24px; font-weight: 600; color: var(--gold);
    border-bottom: 2px solid var(--gold-soft); padding: 0 6px 0 0; line-height: 30px;
  }
  .title-veg { left: 48px; top: 322px; }
  .title-meat { left: 358px; top: 322px; }
  .veg { left: 48px; top: 360px; width: 218px; }
  .veg .price { width: 46px; }
  .meat { left: 358px; top: 360px; width: 224px; }
  .meat .price { width: 48px; }

  .photo-slice {
    position: absolute; left: 287px; top: 728px; width: 302px; height: 140px;
    border-radius: 48% 52% 0 0 / 40% 40% 0 0;
    background: radial-gradient(ellipse at 50% 55%, #6b7a3a 0%, #a07a4a 45%, #e7cfa3 80%, #c9a46d 100%);
  }
  .photo-herbs {
    position: absolute; left: 628px; top: 232px; width: 114px; height: 310px;
    background: radial-gradient(ellipse at center, rgba(160,130,80,0.08), rgba(0,0,0,0) 70%);
  }
  .photo-oven {
    position: absolute; left: 930px; top: 253px; width: 270px; height: 301px;
    background: linear-gradient(160deg, #5a2a1c 0%, #8b3a1e 30%, #f08a1e 55%, #ffc545 70%, #8a3015 90%, #3a1a10 100%);
  }
  .pizza-ring { position: absolute; left: 757px; top: 244px; width: 320px; height: 320px; border-radius: 50%; background: var(--gold); }
  .photo-pizza {
    position: absolute; left: 763px; top: 252px; width: 302px; height: 302px; border-radius: 50%;
    background: radial-gradient(circle at 50% 50%, #e8cf9c 0%, #d9a560 45%, #b8552f 70%, #8a5a35 88%, #6b4a30 100%);
  }
  .arrows { position: absolute; }
  .arrows-top { left: 1018px; top: 233px; }
  .arrows-bottom { left: 1024px; top: 535px; }

  .brand { position: absolute; left: 745px; top: 95px; width: 320px; text-align: center; color: var(--gold); font-family: "Fira Sans", Arial, sans-serif; font-style: normal; font-weight: 600; }
  .brand-name { display: block; font-size: 68px; letter-spacing: 2px; line-height: 1; }
  .brand-sub { display: block; font-size: 24px; letter-spacing: 24px; margin-top: 14px; padding-left: 24px; line-height: 1; }

  .contact { position: absolute; left: 752px; top: 588px; color: var(--cream); font-family: "Cormorant Garamond", Georgia, serif; font-style: normal; }
  .contact-row { display: flex; align-items: center; }
  .contact-row svg { flex: none; width: 44px; }
  .contact-row p { margin-left: 24px; }
  .phone { height: 46px; font-size: 28px; }
  .address { margin-top: 12px; height: 62px; font-size: 25px; line-height: 30px; font-style: italic; }
  .web { margin-top: 12px; height: 40px; font-size: 23px; font-style: italic; }
</style>
</head>
<body>
<main class="flyer">

  <div class="banner banner-desserts">
    <svg viewBox="0 0 262 48" preserveAspectRatio="none"><polygon points="26,0 240,0 232,48 24,48" fill="#c0262d"/><polygon points="0,28 30,18 24,46" fill="#c0262d"/><polygon points="10,6 26,12 28,24" fill="#c0262d"/><polygon points="262,14 236,24 244,44" fill="#c0262d"/><polygon points="236,0 256,4 240,18" fill="#c0262d"/></svg>
    <span>DESSERTS</span>
  </div>
  <div class="banner banner-boissons">
    <svg viewBox="0 0 272 48" preserveAspectRatio="none"><polygon points="26,0 250,0 242,48 24,48" fill="#c0262d"/><polygon points="0,28 30,18 24,46" fill="#c0262d"/><polygon points="10,6 26,12 28,24" fill="#c0262d"/><polygon points="272,14 246,24 254,44" fill="#c0262d"/><polygon points="246,0 266,4 250,18" fill="#c0262d"/></svg>
    <span>BOISSONS</span>
  </div>
  <div class="banner banner-supplements">
    <svg viewBox="0 0 334 48" preserveAspectRatio="none"><polygon points="26,0 312,0 304,48 24,48" fill="#c0262d"/><polygon points="0,28 30,18 24,46" fill="#c0262d"/><polygon points="10,6 26,12 28,24" fill="#c0262d"/><polygon points="334,14 308,24 316,44" fill="#c0262d"/><polygon points="308,0 328,4 312,18" fill="#c0262d"/></svg>
    <span>SUPPLEMENTS</span>
  </div>

  <ul class="menu desserts">
    <li><span class="name">Mousse au chocolat</span><span class="leader"></span><span class="price">7 €</span></li>
    <li><span class="name">Tiramisu: <em>classique, choco</em></span><span class="leader"></span><span class="price">7 €</span></li>
    <li><span class="name">Baba au rhum</span><span class="leader"></span><span class="price">8€</span></li>
    <li><span class="name">Crème brulè</span><span class="leader"></span><span class="price">6,50€</span></li>
    <li><span class="name">Café: <em>expresso</em></span><span class="leader"></span><span class="price">1,8€</span></li>
    <li><span class="name">Thé</span><span class="leader"></span><span class="price">1,5€</span></li>
    <li><span class="name">Capuccino</span><span class="leader"></span><span class="price">2,20€</span></li>
  </ul>

  <section class="drinks">
    <div class="drink-group">
      <div class="drink-head"><span class="name">Boissons 33cl</span><span class="leader"></span><span class="price">2,50 €</span></div>
      <p class="drink-list">Cola, cola zéro, cola cerise, Aranja, Limello, Sunpouch, eau, Tévia, Fruvia, Fruvia pomme cassis</p>
    </div>
    <div class="drink-group">
      <div class="drink-head"><span class="name">Boissons bouteille</span><span class="leader"></span><span class="price">5,50 €</span></div>
      <p class="drink-list">Cola, Aranja, Acqua Vetta, Tévia</p>
    </div>
  </section>

  <h2 class="sub-title title-veg">Legumes &amp; fruits:</h2>
  <h2 class="sub-title title-meat">Viandes:</h2>

  <ul class="menu veg">
    <li><span class="name">Mozza</span><span class="leader"></span><span class="price">1,50€</span></li>
    <li><span class="name">Poivron</span><span class="leader"></span><span class="price">1,50€</span></li>
    <li><span class="name">Burrata</span><span class="leader"></span><span class="price">3,50€</span></li>
    <li><span class="name">Champignon</span><span class="leader"></span><span class="price">2€</span></li>
    <li><span class="name">Buffala</span><span class="leader"></span><span class="price">5€</span></li>
    <li><span class="name">Oignon</span><span class="leader"></span><span class="price">1,50€</span></li>
    <li><span class="name">Chevre</span><span class="leader"></span><span class="price">2€</span></li>
    <li><span class="name">Pomme de terre</span><span class="leader"></span><span class="price">2€</span></li>
    <li><span class="name">st nectaire</span><span class="leader"></span><span class="price">2,50€</span></li>
    <li><span class="name">Aubergine</span><span class="leader"></span><span class="price">2€</span></li>
    <li><span class="name">Gorgonzola</span><span class="leader"></span><span class="price">2€</span></li>
    <li><span class="name">Artichaud</span><span class="leader"></span><span class="price">1,50€</span></li>
    <li><span class="name">Parmesan</span><span class="leader"></span><span class="price">2,50€</span></li>
    <li><span class="name">Courgette</span><span class="leader"></span><span class="price">2€</span></li>
    <li><span class="name">Ricotta</span><span class="leader"></span><span class="price">2€</span></li>
    <li><span class="name">Roquette</span><span class="leader"></span><span class="price">2€</span></li>
    <li><span class="name">Tomate cerise</span><span class="leader"></span><span class="price">2€</span></li>
    <li><span class="name">Pistache</span><span class="leader"></span><span class="price">1€</span></li>
    <li><span class="name">Ail</span><span class="leader"></span><span class="price">1€</span></li>
    <li><span class="name">Olive</span><span class="leader"></span><span class="price">1€</span></li>
    <li><span class="name">Ananas</span><span class="leader"></span><span class="price">2€</span></li>
  </ul>

  <ul class="menu meat">
    <li><span class="name">Poulet</span><span class="leader"></span><span class="price">2,50€</span></li>
    <li><span class="name">Viande hachée</span><span class="leader"></span><span class="price">2,50€</span></li>
    <li><span class="name">Merguez</span><span class="leader"></span><span class="price">2,50€</span></li>
    <li><span class="name">Câpre</span><span class="leader"></span><span class="price">1,50€</span></li>
    <li><span class="name">Jambon cuit</span><span class="leader"></span><span class="price">2€</span></li>
    <li><span class="name">Lardon</span><span class="leader"></span><span class="price">2€</span></li>
    <li><span class="name">Jambon de parme</span><span class="leader"></span><span class="price">3,5€</span></li>
    <li><span class="name">Anchois</span><span class="leader"></span><span class="price">1,50€</span></li>
    <li><span class="name">Thon</span><span class="leader"></span><span class="price">2€</span></li>
    <li><span class="name">œuf</span><span class="leader"></span><span class="price">1€</span></li>
    <li><span class="name">Saumon</span><span class="leader"></span><span class="price">3,50€</span></li>
    <li><span class="name">Chorizo</span><span class="leader"></span><span class="price">2,50€</span></li>
    <li><span class="name">Fruit de mer</span><span class="leader"></span><span class="price">3,50€</span></li>
    <li><span class="name">Scampi</span><span class="leader"></span><span class="price">3,50€</span></li>
    <li><span class="name">Andouillette</span><span class="leader"></span><span class="price">2€</span></li>
    <li><span class="name">Jambon cru</span><span class="leader"></span><span class="price">2€</span></li>
  </ul>

  <div class="photo-slice" role="img" aria-label="Photo d'une pizza à la roquette, jambon cru et copeaux de parmesan"></div>
  <div class="photo-herbs" role="img" aria-label="Dessins discrets d'ingrédients : poivrons, ail, tomates, olives, herbes"></div>

  <div class="brand">
    <span class="brand-name">VORELLO</span>
    <span class="brand-sub">PIZZA</span>
  </div>

  <div class="photo-oven" role="img" aria-label="Photo d'un four à pizza en briques avec flammes"></div>
  <div class="pizza-ring"></div>
  <div class="photo-pizza" role="img" aria-label="Photo d'une pizza garnie sur planche en bois, vue de dessus"></div>

  <svg class="arrows arrows-top" width="166" height="40" viewBox="0 0 166 40">
    <polygon points="0,20 36,0 36,40" fill="#f2c21a"/><polygon points="64,20 100,0 100,40" fill="#f2c21a"/><polygon points="128,20 164,0 164,40" fill="#f2c21a"/>
  </svg>
  <svg class="arrows arrows-bottom" width="166" height="40" viewBox="0 0 166 40">
    <polygon points="0,20 36,0 36,40" fill="#f2c21a"/><polygon points="64,20 100,0 100,40" fill="#f2c21a"/><polygon points="128,20 164,0 164,40" fill="#f2c21a"/>
  </svg>

  <address class="contact">
    <div class="contact-row phone">
      <svg viewBox="0 0 44 44" height="44" fill="none" stroke="#e5b33a" stroke-width="3" stroke-linejoin="round"><path d="M8 4 L15 3 L20 14 L15 18 Q19 28 27 33 L31 28 L41 33 L40 40 Q34 44 26 40 Q10 31 5 14 Q4 8 8 4 Z"/></svg>
      <p>(+352) 26 58 40 71</p>
    </div>
    <div class="contact-row address">
      <svg viewBox="0 0 44 40" height="40" fill="none" stroke="#e5b33a" stroke-width="3" stroke-linejoin="round"><path d="M2 20 L22 3 L42 20"/><path d="M8 15 V38 H36 V15"/><path d="M18 38 V26 H26 V38"/></svg>
      <p>27 rue des tilleuls,<br>L-3829 Kayl, Luxembourg</p>
    </div>
    <div class="contact-row web">
      <svg viewBox="0 0 40 40" height="36" fill="none" stroke="#e5b33a" stroke-width="2.5"><circle cx="20" cy="20" r="17"/><ellipse cx="20" cy="20" rx="8" ry="17"/><path d="M3 20 H37 M6 11 H34 M6 29 H34 M20 3 V37"/></svg>
      <p>www.vorello-example.lu</p>
    </div>
  </address>

</main>
</body>
</html>
```